One Page Advertisement in Tradeshow Brochure

** URGENT DEADLINE - 24 hours **
We are a vendor at a Manufacturing Tradeshow. We are selling Cybersecurity & IT Services to new potential clients in the Manufacturing industry . We need a one page 8x11 layout for the program booklet that will be passed out to attendees at the tradeshow.

We have a basic draft we designed inhouse that needs to be redesigned to look more professional and polished. Please use the information we have on our design as it's all needed to be on the ad. Our ad needs to showcase we are EXPERTS in providing CYBERSECURITY to the Manufacturing Industry. Manufacturing is our top vertical market we service. We also provide IT support as well. Another important detail is to make sure we tell people to visit booth #400 to sign up for a free cybersecurity assessment. The popup bubble is an option. If you can make it work, thats ok AND IF NOT, thats ok too. The message is relevant to what we are educating people on, but whether you can make it look good or not, is an option.

We like the idea of a hacker image. It immediately catches attention and tells people what we are about and what we do.... without talking to us first. I would love a side image of a hacker - if that were possible so that we could use this similar full page ad on a tall skinny pop up banner at our trade show booth. We are purchasing a tall pop up banner for our booth that needs to mimic the full page ad. This will help people identify us at our tradeshow booth because the ad and banner will be designed similar (Same look and feel). The tall pop up banner will be project #2 for you. We can work on that project as soon as the ad is done. I share this #2 project with you so that you know we need another item designed that needs to mirror the booklet advertisement.

This project is VERY URGENT with a 24 hour deadline!! I need this done within 24 hours. I will be readily available to assist with any questions or input throughout the next 24 hours. I have to turn in this ad artwork tomorrow end of day.

We like the idea of a hacker as a main picture/background for the ad. In addition to this full page ad, we will want to take this same info from the 8x11 ad and make a tall pop up banner for our trade show booth. So, there's more project work needed from you (but we have a few extra days before the tall popup banner is required/deadline). The ad is due now and most important. Just be sure to design the ad with the tall popup banner in mind. :) We want them to look very similar.

Thank you!

Target Market(s)

Businesses who need cybersecurity services - our vertical market is manufacturing

Industry/Entity Type

Cybersecurity / Technology / IT Services

Font styles to use
Sans Serif

Colors
0054AA
0677BA
7BADD7
CADEEF
E8F1F8
0094D4
00A9DD
6FCCEA
C7EBF8
E9F6FB
FFF300
FFF600
FEFA6F
FFFEC7
FFFEE8
FFC000
F8CF3A
FAE287
FDF2CF
FEFAEE
EB3D1F
EC4F4E
F09395
F8D3D4
FCEDEE

Requirements
Must have
• all the content on the sample image we provided - with the ex ception of the hacker image and background. Those can be redesigned. Its the wording that has to be included in the design. Feel free to move the wording around and redesign.
Nice to have
• Modern & Clean Fonts - colorful - stand out - techy - cybersecurity - hacker image (you can use a different hacker if you prefer)
Should not have
• No serif type fonts - they are too old and traditional. Don't make the overall design too busy/cluttered

```html
<!DOCTYPE html>
<html lang="en">
<head>
<meta charset="utf-8">
<title>Signal Forge – Tradeshow Ad</title>
<link href="https://fonts.googleapis.com/css2?family=Montserrat:ital,wght@0,400;0,500;0,600;0,700;0,800;0,900;1,900&display=swap" rel="stylesheet">
<style>
  :root{
    --navy:#0c1d3e;
    --navy-deep:#081530;
    --panel:#0f2350;
    --cyan:#3fa3cc;
    --cyan-soft:#6fc6e6;
    --red:#e2232b;
    --white:#ffffff;
    --band:#3b9ec8;
  }
  *{box-sizing:border-box;margin:0;padding:0}
  html,body{width:950px;height:1200px;overflow:hidden;background:var(--navy)}
  body{font-family:"Montserrat",sans-serif;color:var(--white)}
  .ad{position:relative;width:950px;height:1200px;overflow:hidden}
  .hero-photo{position:absolute;inset:0;
    background:
      radial-gradient(ellipse 55% 40% at 30% 75%, rgba(120,190,230,.55), transparent 70%),
      radial-gradient(ellipse 45% 35% at 80% 70%, rgba(110,180,225,.45), transparent 70%),
      radial-gradient(ellipse 35% 30% at 52% 72%, #1e4f8c, transparent 80%),
      linear-gradient(180deg,#0d1f44 0%,#15386e 45%,#1d5a93 75%,#16406f 100%);}
  .frames{position:absolute;inset:0}
  .brand{position:absolute;left:54px;top:53px;display:flex;align-items:center;gap:22px}
  .brand-dot{width:88px;height:88px;border-radius:50%;background:var(--white)}
  .brand-name{font-weight:700;font-size:46px;line-height:.95;letter-spacing:1px;color:var(--white)}
  .delivering{position:absolute;left:560px;top:88px;width:330px;text-align:center;
    font-weight:900;font-style:italic;font-size:38px;letter-spacing:1px}
  .red-copy{position:absolute;right:114px;text-align:right;font-weight:700;font-size:26px;line-height:31px}
  .red-copy.first{top:220px}
  .red-copy.second{top:421px}
  .to{position:absolute;left:806px;top:352px;font-weight:700;font-size:26px}
  .bubble-copy{position:absolute;left:99px;top:292px;font-size:25px;line-height:32px;font-weight:400}
  .bubble-copy b{font-weight:800}
  .ready{position:absolute;left:99px;top:460px;width:343px;height:47px;background:var(--white);
    color:var(--navy);font-weight:800;font-size:34px;line-height:47px;text-align:center}
  .services-title{position:absolute;left:58px;top:605px;font-weight:900;font-size:28px;line-height:29px}
  .service{position:absolute;line-height:1}
  .service .tag{display:block;font-weight:700;font-size:18px;color:var(--cyan)}
  .service .name{display:block;font-size:22px;font-weight:400;margin-top:6px}
  .service.left{left:58px}
  .service.right{right:59px;text-align:right}
  .service.right .tag{padding-right:18px}
  .service.left .tag{padding-left:16px}
  .booth{position:absolute;left:257px;top:803px;width:432px;height:251px;text-align:center}
  .booth-tab{position:absolute;left:127px;top:18px;width:182px;height:35px;background:var(--band);
    color:var(--navy);font-weight:700;font-size:25px;line-height:35px}
  .booth-number{position:absolute;left:0;right:0;top:54px;font-weight:800;font-size:60px;line-height:70px}
  .signup{position:absolute;left:62px;top:121px;width:307px;height:41px;color:var(--navy);
    font-weight:700;font-size:24px;line-height:41px}
  .assessment{position:absolute;left:0;right:0;top:170px;font-size:21px;line-height:27px;font-weight:400}
  .contact{position:absolute;left:0;right:0;top:1100px;display:flex;justify-content:center;gap:18px;
    font-size:14.5px;font-weight:400}
  .contact span{display:flex;align-items:center;gap:5px}
  .contact svg{width:14px;height:14px;fill:none;stroke:var(--white);stroke-width:2}
  .tagline{position:absolute;left:0;right:0;top:1164px;text-align:center;font-size:14px;
    letter-spacing:2.6px;font-weight:500}
</style>
</head>
<body>
<main class="ad">
  <div class="hero-photo" role="img" aria-label="Hooded hacker in a dark blue hoodie working at a laptop, surrounded by blue smoke"></div>

  <svg class="frames" viewBox="0 0 950 1200" aria-hidden="true">
    <!-- delivering badge -->
    <polygon points="590,70 940,70 880,143 525,143" fill="#07142e"/>
    <path d="M560,182 L625,116 L690,116 L700,128 L860,128 L890,122 L930,84 L690,84 L680,72 L620,72 L595,95" fill="none" stroke="var(--cyan)" stroke-width="2.5"/>
    <path d="M540,181 L862,181 L920,122" fill="none" stroke="var(--cyan)" stroke-width="2.5"/>
    <path d="M760,181 L780,196 L802,196 L802,215" fill="none" stroke="var(--cyan)" stroke-width="2.5"/>
    <rect x="797" y="213" width="10" height="10" fill="none" stroke="var(--cyan)" stroke-width="2.5"/>

    <!-- red box one -->
    <polygon points="578,205 862,205 880,222 880,350 590,350 578,338" fill="#0b1a3c" opacity=".92"/>
    <path d="M575,300 L575,195 L832,195 L865,228 L865,323 L645,323" fill="none" stroke="var(--red)" stroke-width="2.5"/>
    <path d="M581,298 L581,202 L610,202" fill="none" stroke="var(--red)" stroke-width="2.5"/>
    <path d="M576,313 L625,338 L775,338 L798,359 L830,359" fill="none" stroke="var(--red)" stroke-width="2.5"/>
    <path d="M858,212 L884,230 L884,300" fill="none" stroke="var(--red)" stroke-width="2.5"/>
    <polygon points="838,353 845,359 838,365 831,359" fill="none" stroke="var(--red)" stroke-width="2.5"/>
    <path d="M852,381 L852,372 L860,372 L860,390 L865,395 L865,410" fill="none" stroke="var(--red)" stroke-width="2.5"/>

    <!-- red box two -->
    <polygon points="585,408 862,408 880,425 880,560 600,560 585,545" fill="#0b1a3c" opacity=".92"/>
    <path d="M575,400 L832,400 L865,433 L865,535 L600,535 L575,510 Z" fill="none" stroke="var(--red)" stroke-width="2.5"/>
    <path d="M581,520 L581,406 L615,406" fill="none" stroke="var(--red)" stroke-width="2.5"/>
    <path d="M858,420 L884,438 L884,523 L862,523" fill="none" stroke="var(--red)" stroke-width="2.5"/>
    <path d="M690,555 L700,555 L722,535" fill="none" stroke="var(--red)" stroke-width="2.5"/>

    <!-- speech bubble -->
    <polygon points="65,300 105,268 475,268 475,603 440,633 410,603 65,603" fill="#0b1b40" opacity=".82"/>
    <path d="M80,617 L80,295 L115,271 L270,271 L300,255 L478,255" fill="none" stroke="var(--cyan)" stroke-width="2.5"/>
    <path d="M478,264 L478,586 L446,618 L414,585 M180,615 L80,615" fill="none" stroke="var(--cyan)" stroke-width="2.5"/>
    <path d="M150,287 L312,287 L330,270 L478,270" fill="none" stroke="var(--cyan)" stroke-width="2.5"/>
    <path d="M99,522 L201,522 L420,717 L444,717" fill="none" stroke="var(--cyan)" stroke-width="2.5"/>
    <polygon points="450,711 456,717 450,723 444,717" fill="none" stroke="var(--cyan)" stroke-width="2.5"/>

    <!-- service leader lines left -->
    <g fill="none" stroke="var(--cyan)" stroke-width="1.6">
      <path d="M0,688 L53,688"/><polygon points="58,684 62,688 58,692 54,688"/>
      <path d="M0,747 L53,747"/><polygon points="58,743 62,747 58,751 54,747"/>
      <path d="M0,806 L53,806"/><polygon points="58,802 62,806 58,810 54,806"/>
      <!-- right -->
      <path d="M896,628 L950,628"/><polygon points="889,624 893,628 889,632 885,628"/>
      <path d="M896,688 L950,688"/><polygon points="889,684 893,688 889,692 885,688"/>
      <path d="M896,747 L950,747"/><polygon points="889,743 893,747 889,751 885,747"/>
      <path d="M896,806 L950,806"/><polygon points="889,802 893,806 889,810 885,806"/>
    </g>

    <!-- booth panel -->
    <rect x="257" y="803" width="432" height="251" rx="6" fill="var(--navy-deep)" opacity=".95"/>
    <polygon points="275,823 672,823 660,1038 283,1040" fill="none" stroke="var(--cyan)" stroke-width="1.6"/>
    <polygon points="377,924 616,924 630,944 616,965 333,965 319,944 333,924" fill="var(--band)"/>

    <!-- bottom bands -->
    <polygon points="0,1055 40,1087 910,1087 950,1053 950,1145 0,1145" fill="var(--band)"/>
    <rect x="0" y="1145" width="950" height="55" fill="#12305d"/>
  </svg>

  <div class="brand">
    <div class="brand-dot"></div>
    <div class="brand-name">signal<br>forge</div>
  </div>

  <div class="delivering">DELIVERING</div>

  <div class="red-copy first">MANAGED IT<br>CYBERSECURITY<br>SERVICES</div>
  <div class="to">TO</div>
  <div class="red-copy second">THE<br>MANUFACTURING<br>INDUSTRY</div>

  <p class="bubble-copy">IT’S NOT A MATTER OF IF<br>YOU WILL <b>GET HACKED</b><br>IT’S A <b>MATTER</b> OF<br>WHEN YOU&nbsp; GET<br>HACKED!</p>
  <div class="ready">ARE YOU READY?</div>

  <h2 class="services-title">IT SERVICES<br>PROVIDED</h2>
  <div class="service left" style="top:679px"><span class="tag">Managed</span><span class="name">Cybersecurity</span></div>
  <div class="service left" style="top:738px"><span class="tag">Fully</span><span class="name">Managed IT</span></div>
  <div class="service left" style="top:797px"><span class="tag">CO-</span><span class="name">Managed IT</span></div>

  <div class="service right" style="top:619px"><span class="tag">Cloud</span><span class="name">Services</span></div>
  <div class="service right" style="top:679px"><span class="tag">Business</span><span class="name">Continuity</span></div>
  <div class="service right" style="top:738px"><span class="tag">IT</span><span class="name">Projects</span></div>
  <div class="service right" style="top:797px"><span class="tag">Phone</span><span class="name">Service</span></div>

  <section class="booth">
    <div class="booth-tab">Visit Booth</div>
    <div class="booth-number">#400</div>
    <div class="signup">Sign Up For A Free</div>
    <p class="assessment">CYBERSECURITY ASSESSMENT<br>($2500 Value) 400</p>
  </section>

  <div class="contact">
    <span><svg viewBox="0 0 16 16"><path d="M8 15s5-5 5-9a5 5 0 0 0-10 0c0 4 5 9 5 9z"/><circle cx="8" cy="6" r="1.6"/></svg>4420 Cedar Ridge Pkwy. Austin, TX 78731</span>
    <span><svg viewBox="0 0 16 16"><path d="M3 2l3 0 1 4-2 1a8 8 0 0 0 4 4l1-2 4 1 0 3a2 2 0 0 1-2 1A12 12 0 0 1 1 4a2 2 0 0 1 2-2z"/></svg>(512) 555-0148 (SFIT)</span>
    <span><svg viewBox="0 0 16 16"><rect x="1" y="3" width="14" height="10"/><path d="M1 3l7 6 7-6"/></svg>support@sfit.example</span>
    <span><svg viewBox="0 0 16 16"><circle cx="8" cy="8" r="6.5"/><path d="M1.5 8h13M8 1.5c-3 3.5-3 9.5 0 13M8 1.5c3 3.5 3 9.5 0 13"/></svg>www.sfit.example</span>
  </div>

  <p class="tagline">Multi Award Winning IT Delivered By PEOPLE.&nbsp; PROCESSES.&nbsp; TECHNOLOGY.</p>
</main>
</body>
</html>
```